New website for engineering consultant

We need to update our existing web site. We've just had our logo re-done and have attached it.

We are an engineering consulting firm that specialises in mechanical and structural engineering, design and drafting. Our customers are other businesses in the manufacturing, mining and agricultural industries.

We would like the designs to be professional and highlight that we are innovative.

Industry/Entity Type

Mining

Requirements
Must have
• A module that rotates pictures so we can showcase certain projects. We have attached a few rendered images of projects for you to play with.

```html
<!DOCTYPE html>
<html lang="en">
<head>
<meta charset="utf-8">
<title>Torqline — Engineering Consulting</title>
<link rel="stylesheet" href="https://fonts.googleapis.com/css2?family=Source+Sans+3:wght@200;400;600;700&display=swap">
<style>
:root{
  --blue:#1d3f9e;
  --blue-link:#1b44b5;
  --news-link:#3d78c8;
  --grey-text:#8a8a8a;
  --dark-text:#333;
  --nav-text:#1c2f73;
  --rule:#d6d6d6;
  --panel:#eeeeee;
  --panel-border:#c9c9c9;
  --news-head:#7e818d;
  --news-body:#dde0ec;
  --footer:#2f2b29;
  --footer-text:#9a9693;
  --search:#3c4148;
  --font:"Source Sans 3", "Myriad Pro", Arial, sans-serif;
}
*{box-sizing:border-box;margin:0;padding:0}
html,body{width:1200px;height:1024px;overflow:hidden;background:#fff;font-family:var(--font)}
.page{position:relative;width:1200px;height:1024px}

.call-box{position:absolute;left:851px;top:-1px;width:239px;height:32px;border:1px solid #bdbdbd;border-top:none;border-radius:0 0 5px 5px;background:linear-gradient(#fff,#ececec);display:flex;align-items:center;justify-content:center;gap:6px;font-size:19px}
.call-box .label{color:#666}
.call-box .number{color:var(--blue-link)}

.brand{position:absolute;left:112px;top:38px;display:flex;align-items:center;gap:14px}
.brand-dot{width:48px;height:48px;border-radius:50%;background:var(--blue)}
.brand-name{font-size:38px;font-weight:700;color:var(--blue);letter-spacing:-.5px}

.nav{position:absolute;left:0;top:113px;width:1200px;height:57px;background:linear-gradient(#f1f1f1,#fff 60%);border-top:1px solid #e5e5e5}
.nav ul{list-style:none;position:absolute;left:113px;top:0;display:flex;height:56px}
.nav li{height:56px;display:flex;align-items:center;justify-content:center;border-right:1px solid var(--rule);font-size:13px;color:var(--nav-text);text-transform:uppercase}
.nav li:first-child{border-left:1px solid var(--rule);font-weight:700;background:#fff}
.search{position:absolute;left:859px;top:19px;width:229px;height:23px;background:var(--search);border-radius:3px;color:#ddd;font-size:11px;font-style:italic;padding:3px 8px}
.search svg{position:absolute;right:10px;top:3px}

.hero{position:absolute;left:0;top:170px;width:1200px;height:344px;background:linear-gradient(#c9d6e0,#eef1f4 45%,#b8b2a6 80%,#8b8478);border-bottom:1px solid #9a9a9a}
.hero-caption{position:absolute;left:716px;top:57px;width:375px;height:117px;background:rgba(70,70,72,.88);border-radius:7px 0 0 7px;padding:11px 18px;color:#fff}
.hero-caption h2{font-size:19px;font-weight:600;line-height:22px}
.hero-caption p{font-size:18px;line-height:26px}
.hero-dots{position:absolute;left:1028px;top:322px;display:flex;gap:5px}
.hero-dots span{width:10px;height:10px;border-radius:50%;background:#fff}

.welcome{position:absolute;left:112px;top:532px;width:680px}
.welcome h1{font-size:37px;font-weight:200;color:#111;letter-spacing:-.5px}
.welcome h1 strong{font-weight:600;color:var(--blue)}
.welcome p{margin-top:10px;font-size:12.3px;line-height:16px;color:var(--grey-text);font-weight:600}

.news{position:absolute;left:825px;top:534px;width:265px;height:152px;background:var(--news-body);border-radius:3px;overflow:hidden}
.news h3{height:36px;background:var(--news-head);color:#fff;font-size:17px;font-weight:600;padding:8px 10px}
.news .headline{margin:12px 8px 0;font-size:11.5px;line-height:13px;color:var(--news-link);font-weight:600;text-transform:uppercase}
.news .summary{margin:4px 10px 0;font-size:11.5px;line-height:14px;color:var(--dark-text);width:220px}
.news .date{position:absolute;right:10px;bottom:5px;font-size:11px;color:var(--dark-text)}

.projects{position:absolute;left:114px;top:706px;width:974px;height:222px;background:var(--panel);border:1px solid var(--panel-border)}
.arrow{position:absolute;top:70px}
.project{position:absolute;top:31px;width:178px}
.project .thumb{width:178px;height:110px;background:linear-gradient(#fff,#ececec);border:1px solid #bbb}
.project h4{margin:2px 2px 0;font-size:13px;font-weight:400;color:var(--blue-link)}
.project p{margin-left:1px;font-size:11px;line-height:14px;color:var(--grey-text)}
.project .more{display:flex;align-items:center;gap:4px;margin:10px 2px 0;font-size:11px;color:#222}

.footer{position:absolute;left:0;top:968px;width:1200px;height:56px;background:var(--footer);text-align:center;color:var(--footer-text);font-size:12px;padding-top:10px;line-height:17px}
</style>
</head>
<body>
<div class="page">
  <header>
    <div class="call-box"><span class="label">Call Now :</span><span class="number">555-010-2486</span></div>
    <div class="brand"><span class="brand-dot"></span><span class="brand-name">TORQLINE</span></div>
  </header>

  <nav class="nav">
    <ul>
      <li style="width:81px">New Desk</li>
      <li style="width:118px">About Us</li>
      <li style="width:123px">Capabilities</li>
      <li style="width:97px">Sectors</li>
      <li style="width:100px">Projects</li>
      <li style="width:106px">Careers</li>
      <li style="width:106px;border-right:none">Contacts</li>
    </ul>
    <div class="search">Search
      <svg width="18" height="17" viewBox="0 0 18 17"><circle cx="7" cy="7" r="5.5" fill="none" stroke="#fff" stroke-width="2"/><line x1="11" y1="11" x2="16" y2="16" stroke="#fff" stroke-width="2.5" stroke-linecap="round"/></svg>
    </div>
  </nav>

  <section class="hero" role="img" aria-label="Two engineers in orange hi-vis gear and hard hats reviewing a tablet at a mine site with heavy machinery under a cloudy sky">
    <div class="hero-caption">
      <h2>ENGINEERING CONSULTING</h2>
      <p>Life and times are ever changing. Adapt-ing to the changing needs and demands is growth</p>
    </div>
    <div class="hero-dots"><span></span><span></span><span></span><span></span></div>
  </section>

  <section class="welcome">
    <h1>Welcome to <strong>TORQLINE</strong></h1>
    <p>Lorem Ipsum is simply dummy text of the printing and typesetting industry. Lorem Ipsum has been the industry's standard dummy text ever since the 1500s, when an unknown printer took a galley of type and scrambled it to make a type specimen book. It has survived not only five centuries, but also the leap into electronic typesetting, remaining essentially unchanged. It was popularised in the 1960s with the release of Linotext sheets containing Lorem Ipsum passages, and more recently with desktop publishing software like Paginate Studio including versions of Lorem Ipsum.</p>
  </section>

  <aside class="news">
    <h3>LATEST NEWS</h3>
    <p class="headline">Lorem ipsum is simply dummy text of the printing and typesetting i</p>
    <p class="summary">Lorem Ipsum is simply dummy text of the printing and typesetting industry. Lorem Ipsum has been the industry's</p>
    <p class="date">11 January 2012</p>
  </aside>

  <section class="projects">
    <svg class="arrow" style="left:12px" width="16" height="32" viewBox="0 0 16 32"><path d="M14 2 L2 16 L14 30 Z" fill="#3a3a3a"/></svg>
    <svg class="arrow" style="left:940px" width="16" height="32" viewBox="0 0 16 32"><path d="M2 2 L14 16 L2 30 Z" fill="#3a3a3a"/></svg>

    <article class="project" style="left:48px">
      <div class="thumb" role="img" aria-label="Render of a steel access platform with stairs"></div>
      <h4>Lorem Lipsum</h4><p>Vertical and Horizontal Machining Centers</p>
      <div class="more">Read more <svg width="11" height="8" viewBox="0 0 11 8"><path d="M1 1l3 3-3 3M6 1l3 3-3 3" fill="none" stroke="#1a8a4a" stroke-width="1.8"/></svg></div>
    </article>
    <article class="project" style="left:284px;top:32px">
      <div class="thumb" role="img" aria-label="Render of a cable drum on a steel frame"></div>
      <h4>Simply Dummy</h4><p>Vertical and Horizontal Machining Centers</p>
      <div class="more">Read more <svg width="11" height="8" viewBox="0 0 11 8"><path d="M1 1l3 3-3 3M6 1l3 3-3 3" fill="none" stroke="#1a8a4a" stroke-width="1.8"/></svg></div>
    </article>
    <article class="project" style="left:508px;top:32px">
      <div class="thumb" role="img" aria-label="Render of a yellow streamlined pod"></div>
      <h4>Dummy text</h4><p>Vertical and Horizontal Machining Centers</p>
      <div class="more">Read more <svg width="11" height="8" viewBox="0 0 11 8"><path d="M1 1l3 3-3 3M6 1l3 3-3 3" fill="none" stroke="#1a8a4a" stroke-width="1.8"/></svg></div>
    </article>
    <article class="project" style="left:737px;top:33px">
      <div class="thumb" role="img" aria-label="Render of a vehicle bull bar"></div>
      <h4>Lorem Lipsum</h4><p>Vertical and Horizontal Machining Centers</p>
      <div class="more">Read more <svg width="11" height="8" viewBox="0 0 11 8"><path d="M1 1l3 3-3 3M6 1l3 3-3 3" fill="none" stroke="#1a8a4a" stroke-width="1.8"/></svg></div>
    </article>
  </section>

  <footer class="footer">
    Newdesk | About us | Capabilties | Sectors | Projects | Careers | Contact Us<br>
    © Copyright 2012 by Engineering Consultant
  </footer>
</div>
</body>
</html>
```